Fern Tower AG – The secret mission

Hi all. We would love to enhance our website and the sales funnel like on our website www.ferntower.ch
We are looking for a clean and fresh design which is reflecting our
two main passions: "gaming and investing".
For infos pls have a look at the website www.ferntower.ch, our youtube channel.
You find many info attached. We are curious how you interprete the topic.

Target Market(s)

Gamers | Investor - worldwide market

Industry/Entity Type

Games

Number of Pages Required

5+ page

Requirements
Must have
• 6 Sites, fresh and modern design (gaming)
Nice to have
• sales funnel (Get involved page) in the same design, webshop
Should not have
• Our shares are on a blockchain, which are very modern (www.plimex.ch). So blockchain design is okay but please no affiliation to bitcoin or crytpocurrencies. thx.

```html
<!DOCTYPE html>
<html lang="en">
<head>
<meta charset="utf-8">
<title>Fern Tower AG – The Secret Mission</title>
<link href="https://fonts.googleapis.com/css2?family=Open+Sans:wght@400;600;700&family=Roboto:wght@400;500&display=swap" rel="stylesheet">
<style>
:root{
  --red:#d7132a;
  --blue:#4a5db0;
  --navy:#0b1a4d;
  --ink:#1a1a1a;
  --grey:#6b6b6b;
  --light:#eeeff1;
  --white:#fff;
  --black:#050505;
}
*{box-sizing:border-box;margin:0;padding:0}
html,body{width:1200px;height:4203px;overflow:hidden;background:var(--white)}
body{position:relative;font-family:"Open Sans",sans-serif;color:var(--ink)}
.abs{position:absolute}
.btn{position:absolute;display:flex;align-items:center;justify-content:center;border-radius:24px;color:var(--white);font:700 13px "Roboto",sans-serif;text-transform:uppercase}
.btn-red{background:var(--red)}
/* header */
.site-header{position:absolute;left:0;top:0;width:1200px;height:120px;background:var(--white);border-top:3px solid var(--blue);z-index:3}
.brand{position:absolute;left:100px;top:0;width:172px;height:165px;border-radius:0 0 86px 86px;background:var(--white);display:flex;align-items:center;justify-content:center;gap:6px;z-index:4}
.brand-dot{width:14px;height:14px;border-radius:50%;background:var(--red)}
.brand-name{font:700 17px "Open Sans",sans-serif;color:var(--red)}
.call{position:absolute;left:480px;top:22px;display:flex;align-items:center;gap:8px;font:400 13px "Roboto",sans-serif}
.call b{font-size:19px;font-weight:400}
.nav{position:absolute;top:82px;left:376px;display:flex;gap:36px;font:400 13px "Roboto",sans-serif;text-transform:uppercase}
.nav .active{color:var(--red);border-bottom:3px solid var(--red);padding-bottom:6px}
/* hero */
.hero{position:absolute;left:0;top:120px;width:1200px;height:700px;background:linear-gradient(180deg,#000 0%,#000 30%,#061240 65%,#1345b8 90%,#0b2a80 100%)}
.hero-title{position:absolute;top:215px;width:1200px;text-align:center;color:var(--white);font:700 44px/52px "Open Sans",sans-serif;text-transform:uppercase}
.hero-badge{position:absolute;left:565px;top:150px;width:70px;height:70px;border-radius:50%;border:3px solid var(--white)}
.dots{position:absolute;top:590px;left:565px;display:flex;gap:8px}
.dots i{width:11px;height:11px;border-radius:50%;background:var(--white)}
.dots i.on{background:var(--red)}
.mission{position:absolute;left:0;top:720px;width:1200px;height:602px;background:var(--light)}
.h2{font:700 46px/52px "Open Sans",sans-serif;text-transform:uppercase}
.body-s{font-size:12px;line-height:22px;color:var(--grey)}
/* about */
.about-title{position:absolute;top:1400px;width:1200px;text-align:center}
.about-text{position:absolute;left:170px;top:1478px;width:860px;text-align:center}
.about-text p+p{margin-top:22px}
.ring{position:absolute;width:264px;height:264px;border-radius:50%;border:5px solid var(--red);background:var(--white)}
.ring span{position:absolute;left:12px;top:12px;width:230px;height:230px;border-radius:50%}
/* story */
.story-title{position:absolute;left:112px;top:2180px;color:var(--white);font:700 30px/43px "Open Sans",sans-serif;text-transform:uppercase}
.story-text{position:absolute;left:112px;top:2285px;width:470px;color:var(--white);font-size:11.5px;line-height:22px}
.story-text p+p{margin-top:22px}
.video{position:absolute;left:617px;top:2192px;width:471px;height:340px;border-radius:30px;background:linear-gradient(135deg,#7a8ea8,#4d5a6b 50%,#a09080)}
/* posts */
.section-title{font:700 30px "Open Sans",sans-serif;text-transform:uppercase}
.card{position:absolute;top:2783px;width:228px;height:286px;background:var(--white);border-radius:10px;box-shadow:0 2px 8px rgba(0,0,0,.12)}
.card span{position:absolute;left:7px;top:7px;right:7px;height:163px;border-radius:8px}
.card h3{position:absolute;left:22px;top:185px;right:14px;font:600 14.5px/26px "Open Sans",sans-serif;color:#222}
/* faq */
.faq-item{position:absolute;left:600px;width:488px;height:64px;background:#f0f0f2;display:flex;align-items:center;justify-content:space-between;padding:0 26px;font:600 19px "Open Sans",sans-serif;color:#222;box-shadow:0 1px 3px rgba(0,0,0,.12)}
.plus{width:17px;height:17px;border-radius:50%;background:var(--red);position:relative}
.plus:before,.plus:after{content:"";position:absolute;background:var(--white);left:4px;top:7.5px;width:9px;height:2px}
.plus:after{transform:rotate(90deg)}
.link{font-size:12px;color:#2b55c9;text-decoration:underline}
/* footer */
.footer{position:absolute;left:0;top:3700px;width:1200px;height:503px;background:var(--black);color:var(--white)}
.foot-h{position:absolute;top:140px;font:700 15px "Open Sans",sans-serif}
.field{position:absolute;background:var(--white);color:#888;font:400 10px "Roboto",sans-serif;padding:8px 10px;text-transform:uppercase}
.links{position:absolute;left:668px;top:180px;list-style:none;font:400 12px "Roboto",sans-serif}
.links li{height:32.5px}
.links li:before{content:"»";margin-right:12px}
.contact{position:absolute;left:833px;top:175px;font:400 12px/16px "Roboto",sans-serif}
.contact div{display:flex;align-items:center;gap:16px;height:48px}
.cicon{width:34px;height:34px;border-radius:50%;border:2px solid var(--white);flex:none;display:flex;align-items:center;justify-content:center}
.social{position:absolute;top:4142px;width:30px;height:30px;border-radius:50%;border:2px solid var(--white)}
</style>
</head>
<body>

<header class="site-header">
  <div class="call">
    <svg width="26" height="30" viewBox="0 0 26 30"><path d="M6 3c2-1 4 3 5 6s-2 3-1 6 4 7 6 7 3-3 5-1 3 4 1 5c-6 4-12-2-15-8S2 5 6 3z" fill="var(--blue)"/></svg>
    <span>Call us Today : <b>+1 888 888 8888</b></span>
  </div>
  <div class="btn" style="left:805px;top:14px;width:117px;height:44px;background:var(--blue)">&#9679;&nbsp; Login</div>
  <div class="btn btn-red" style="left:935px;top:14px;width:153px;height:44px">Get a Quote</div>
  <nav class="nav">
    <span class="active">Home</span><span>About Us</span><span>Get Involved</span><span style="margin-left:0">Frequently Asked Questions</span><span>Press</span><span>Contact Us</span>
  </nav>
</header>
<div class="brand"><span class="brand-dot"></span><span class="brand-name">Fern Tower AG</span></div>

<section class="hero" role="img" aria-label="Glowing blue network of cubes over a dark background">
  <div class="hero-badge"></div>
  <h1 class="hero-title">Fern Tower AG is a<br>Swiss holding company</h1>
  <div class="btn btn-red" style="left:524px;top:342px;width:152px;height:46px;border-radius:23px">Get Started</div>
  <div class="dots"><i></i><i class="on"></i><i></i><i></i></div>
</section>

<section class="mission">
  <svg class="abs" style="left:0;top:-20px" width="1200" height="120" viewBox="0 0 1200 120"><path d="M0 0 Q600 140 1200 0 V120 H0Z" fill="var(--light)"/><path d="M0 4 Q600 144 1200 4" fill="none" stroke="var(--red)" stroke-width="5"/></svg>
  <div class="abs" style="left:120px;top:250px;display:flex;align-items:center;gap:14px">
    <span style="width:40px;height:40px;border-radius:50%;background:var(--red)"></span>
    <span style="font:700 44px 'Open Sans',sans-serif;color:var(--navy)">FERN TOWER AG</span>
  </div>
  <h2 class="h2 abs" style="left:600px;top:252px">Fern Tower AG –<br>The secret mission</h2>
  <p class="body-s abs" style="left:600px;top:366px;width:470px">We are an investment holding with the pupose to invest in FinTech in gaming, to enhance the gaming experience and to build the tools to unite the gamers to enjoy their games.</p>
</section>

<h2 class="h2 about-title">About us</h2>
<div class="about-text body-s">
  <p>Fern Tower AG is a Swiss holding company, investing in the booming online videogame sector. Our main focus centres on the gaming community. Our highest priority is the TradeVault software – the First International Play Money Exchange. TradeVault has developed a next-generation disruptive virtual asset exchange to help online video game players easily and securely value and trade their in-game virtual money, items and services between games worlds or for cash. This will bring the real-world and virtual economies closer together. Gamers will have the opportunity to make money with, and from, their passion in videogames.</p>
  <p>Fern Tower AG is founded by Lukas Brenner and Mario Castell, and the initial shareholders of TradeVault. The company is based in the Lakeside centre in Seewil, Switzerland. Shares of Fern Tower AG are listed on Plimex, the digital share platform in Switzerland. Shares are secured on the Plimex blockchain, powered by Alpnet.</p>
</div>
<div class="ring" style="left:98px;top:1700px"><span role="img" aria-label="Hands counting banknotes" style="background:radial-gradient(#e8c98a,#8a7a6a)"></span></div>
<div class="ring" style="left:343px;top:1700px"><span role="img" aria-label="Hands planting a seedling in soil" style="background:radial-gradient(#7da04a,#4a3528)"></span></div>
<div class="ring" style="left:588px;top:1700px"><span role="img" aria-label="Person holding a fan of banknotes" style="background:radial-gradient(#d8a670,#6a6f66)"></span></div>
<div class="ring" style="left:836px;top:1700px"><span role="img" aria-label="Wallet filled with colourful banknotes" style="background:radial-gradient(#7aa06a,#141414)"></span></div>

<svg class="abs" style="left:0;top:2050px" width="1200" height="585" viewBox="0 0 1200 585" role="img" aria-label="Dark blue band with a faint network globe">
  <defs><radialGradient id="navyGlow" cx="0.5" cy="1" r="0.9"><stop offset="0" stop-color="#1c3a8a"/><stop offset="1" stop-color="#07133d"/></radialGradient></defs>
  <path d="M0 90 Q600 -40 1200 90 V585 H0Z" fill="url(#navyGlow)"/>
</svg>
<h2 class="story-title">Whats the story with the<br>name “Fern Tower”?</h2>
<div class="story-text">
  <p>One of the first online games was called Dungeon Reign – a “hack n slay” game that was an enormous success, launched in the mid 1990’s.</p>
  <p>The large Dungeon Reign player community made up a rumour that there was a secret “Fern Tower” accessible only by repeatedly clicking on the ferns that could be found just outside town. The Fern Tower being the place where you could find the best treasure (this being one of the main objectives in the game, to get better gear).</p>
  <p>Years later, Frostpeak, the developer of the game, integrated the “fern fern tower” into the sequel “Dungeon Reign 2” as a nod toward the years of jokes about the legendary secret level; the community kept on calling it the “Fern Tower”.</p>
</div>
<div class="video" role="img" aria-label="Video still of two founders talking by a harbour window">
  <svg class="abs" style="left:214px;top:150px" width="34" height="38" viewBox="0 0 34 38"><path d="M2 2 L32 19 L2 36Z" fill="var(--white)"/></svg>
</div>

<h2 class="section-title abs" style="top:2718px;width:1200px;text-align:center">Recent Posts</h2>
<div class="card" style="left:112px"><span role="img" aria-label="Hands holding banknotes" style="background:linear-gradient(135deg,#4a4a4a,#e0a060)"></span><h3>The History and the Team Behind TradeVault: Interview with Founders, Part 1</h3></div>
<div class="card" style="left:360px"><span role="img" aria-label="Figure planting a Swiss flag at sunset" style="background:linear-gradient(180deg,#a9a9a0,#d0372f 60%,#555)"></span><h3>The Ingame Items Market is Broken... But Here’s How it Can Be Fixed</h3></div>
<div class="card" style="left:610px"><span role="img" aria-label="Smiling man holding banknotes" style="background:linear-gradient(135deg,#8fb4c0,#c09070)"></span><h3>Why the Ingame Items Market is Broken: a Gamer’s and Trader’s</h3></div>
<div class="card" style="left:858px"><span role="img" aria-label="Hands forming a heart around a Swiss cross" style="background:linear-gradient(135deg,#f4eeee,#e39a9a)"></span><h3>What Types of Downloadable Ingame Content Are There and Why</h3></div>
<div class="btn btn-red" style="left:524px;top:3103px;width:152px;height:46px">View More &nbsp;&#10148;</div>

<h2 class="section-title abs" style="left:108px;top:3234px">Our Portfolio</h2>
<div class="abs" style="left:110px;top:3330px;display:flex;align-items:center;gap:8px"><span style="width:20px;height:20px;background:var(--blue)"></span><span style="font:700 22px 'Open Sans',sans-serif;color:#222">TradeVault</span></div>
<div class="abs" style="left:262px;top:3330px;display:flex;align-items:center;gap:10px"><span style="width:30px;height:30px;border-radius:50%;background:#111"></span><span style="font:700 30px 'Open Sans',sans-serif;color:#111">nodeline</span></div>
<span class="link abs" style="left:108px;top:3461px">www.tradevault.de</span>
<span class="link abs" style="left:272px;top:3461px">www.nodeline.com</span>

<h2 class="section-title abs" style="left:598px;top:3234px">Frequently Asked Questions</h2>
<div class="faq-item" style="top:3300px">What are tokenised shares?<i class="plus"></i></div>
<div class="faq-item" style="top:3380px">What is the link betwen TradeVault<i class="plus"></i></div>
<div class="faq-item" style="top:3460px">What is TradeVault?<i class="plus"></i></div>
<div class="faq-item" style="top:3540px">What is Fern Tower AG<i class="plus"></i></div>

<footer class="footer">
  <svg class="abs" style="left:0;top:0" width="1200" height="90" viewBox="0 0 1200 90"><path d="M0 0 H1200 V70 Q600 -30 0 70Z" fill="var(--white)"/><path d="M0 76 Q600 -24 1200 76" fill="none" stroke="var(--red)" stroke-width="5"/></svg>
  <div class="foot-h" style="left:112px">Get In Involved:</div>
  <div class="field" style="left:115px;top:175px;width:240px;height:31px">Name :</div>
  <div class="field" style="left:365px;top:175px;width:240px;height:31px">Phone :</div>
  <div class="field" style="left:115px;top:218px;width:490px;height:31px">Email :</div>
  <div class="field" style="left:115px;top:260px;width:490px;height:72px">Message :</div>
  <div class="btn btn-red" style="left:523px;top:353px;width:84px;height:29px;border-radius:6px;font-size:12px">Submit</div>
  <div class="foot-h" style="left:665px">Useful Links</div>
  <ul class="links"><li>Home</li><li>About Us</li><li>Get Involved</li><li>FAQ</li><li>Press</li><li>Contact Us</li></ul>
  <div class="foot-h" style="left:833px">Contact Information</div>
  <div class="contact">
    <div><span class="cicon"><svg width="12" height="16" viewBox="0 0 12 16"><path d="M6 0a6 6 0 0 1 6 6c0 4-6 10-6 10S0 10 0 6a6 6 0 0 1 6-6z" fill="var(--white)"/><circle cx="6" cy="6" r="2" fill="var(--black)"/></svg></span><span>Lorem ipsum dolor sit amet,<br>consectetur adipiscing elit, sed do</span></div>
    <div><span class="cicon"><svg width="14" height="14" viewBox="0 0 26 30"><path d="M6 3c2-1 4 3 5 6s-2 3-1 6 4 7 6 7 3-3 5-1 3 4 1 5c-6 4-12-2-15-8S2 5 6 3z" fill="var(--white)"/></svg></span><span>Phone : +1 888 888 8888</span></div>
    <div><span class="cicon"><svg width="14" height="10" viewBox="0 0 14 10"><rect width="14" height="10" fill="var(--white)"/><path d="M0 0 L7 6 L14 0" fill="none" stroke="var(--black)"/></svg></span><span>Email : info@companyname.com</span></div>
    <div><span class="cicon"><svg width="14" height="14" viewBox="0 0 14 14"><rect x="1" y="4" width="12" height="9" fill="var(--white)"/><rect x="4" y="0" width="6" height="5" fill="none" stroke="var(--white)" stroke-width="1.5"/></svg></span><span>Fax: 0661-23045</span></div>
  </div>
  <div class="abs" style="left:105px;top:420px;width:1000px;height:1px;background:#333"></div>
  <div class="abs" style="left:115px;top:450px;font:400 11px 'Roboto',sans-serif">Copyright © 2021 Company name - All Rights Reserved.</div>
</footer>
<span class="social" style="left:990px"></span>
<span class="social" style="left:1026px;background:var(--red);border-color:var(--red)"></span>
<span class="social" style="left:1062px"></span>

</body>
</html>
```